Kestrel & Dunmore Varnell Cargomax 2400

Need to create a wrap that really POPS. The customer is a home contractor. His website is https://kestreldunmore.com/
He wants the wrap to capture everything he creates. The work truck is a 2012 Varnell Cargomax box truck 3500. The box is 12ft wide x 86" tall. The rear door is 70" tall x 70" wide. He wants to incorporate red/gray/black into the logo and design. Also, he likes the attached wrap design. Use that for inspiration, please do not copy directly.

```html
<!DOCTYPE html>
<html lang="en">
<head>
<meta charset="utf-8">
<title>Kestrel &amp; Dunmore – Varnell Cargomax 2400 Wrap</title>
<link rel="stylesheet" href="https://fonts.googleapis.com/css2?family=Archivo+Black&family=Archivo:wght@600;700&family=Anton&display=swap">
<style>
  :root {
    --wrap-red: #e31b1f;
    --wrap-gray: #8d8e92;
    --wrap-black: #141414;
    --wrap-white: #ffffff;
    --ink-dark: #3a2a2e;
    --ink-soft: #5b5b5f;
    --canvas-bg: #e7e8ea;
  }
  html, body {
    margin: 0;
    padding: 0;
    width: 1200px;
    height: 2666px;
    overflow: hidden;
    background: var(--canvas-bg);
  }
  .wrap-sheet {
    position: relative;
    width: 1200px;
    height: 2666px;
  }
  .panel {
    position: absolute;
    display: block;
    box-shadow: 0 2px 10px rgba(0,0,0,0.15);
  }
  .panel--side { left: 40px; top: 60px; width: 1120px; height: 670px; }
  .panel--rear { left: 210px; top: 880px; width: 780px; height: 780px; }
  .panel--door { left: 40px; top: 1860px; width: 400px; height: 400px; }
  .panel--hood { left: 500px; top: 1910px; width: 660px; height: 300px; }
  .brand-name { font-family: "Archivo Black", sans-serif; }
  .services { font-family: "Archivo", sans-serif; font-weight: 700; }
  .phone { font-family: "Archivo Black", sans-serif; }
  .phone--rear { font-family: "Anton", sans-serif; }
  .tagline { font-family: "Archivo", sans-serif; font-weight: 600; }
  .web-address { font-family: "Archivo", sans-serif; font-weight: 700; }
</style>
</head>
<body>
<main class="wrap-sheet">

  <svg class="panel panel--side" viewBox="0 0 1120 670" xmlns="http://www.w3.org/2000/svg">
    <rect class="side-base" width="1120" height="670" fill="var(--wrap-white)"/>
    <polygon class="side-gray-field" points="0,0 690,0 540,170 0,170" fill="var(--wrap-gray)"/>
    <polygon class="side-black-stripe" points="660,0 700,0 1120,292 1120,330" fill="var(--wrap-black)"/>
    <polygon class="side-red-band" points="720,0 1120,0 1120,276" fill="var(--wrap-red)"/>
    <text class="web-address" x="960" y="110" font-size="32" fill="var(--wrap-white)" text-anchor="middle" transform="rotate(34.6 960 110)">kestreldunmore.com</text>
    <text class="brand-name" x="600" y="300" font-size="66" fill="var(--ink-dark)" text-anchor="middle">KESTREL &amp;</text>
    <text class="brand-name" x="600" y="380" font-size="66" fill="var(--ink-dark)" text-anchor="middle">DUNMORE</text>
    <text class="services" x="600" y="432" font-size="27" fill="var(--wrap-black)" text-anchor="middle">KITCHEN | BATHROOM | HOME REPAIR</text>
    <text class="phone" x="30" y="610" font-size="46" fill="var(--ink-dark)">555 014 7720</text>
    <text class="tagline" x="1090" y="580" font-size="21" fill="var(--wrap-black)" text-anchor="end">MEASURED TWICE,</text>
    <text class="tagline" x="1090" y="610" font-size="21" fill="var(--wrap-black)" text-anchor="end">BUILT TO LAST FOR YEARS</text>
  </svg>

  <svg class="panel panel--rear" viewBox="0 0 780 780" xmlns="http://www.w3.org/2000/svg">
    <rect class="rear-base" width="780" height="780" fill="var(--wrap-white)"/>
    <rect class="rear-red-field" width="780" height="560" fill="var(--wrap-red)"/>
    <rect class="rear-black-stripe" y="560" width="780" height="14" fill="var(--wrap-black)"/>
    <text class="brand-name" x="390" y="200" font-size="62" fill="var(--wrap-white)" text-anchor="middle">KESTREL &amp;</text>
    <text class="brand-name" x="390" y="270" font-size="62" fill="var(--wrap-white)" text-anchor="middle">DUNMORE</text>
    <text class="services" x="390" y="318" font-size="25" fill="var(--wrap-white)" text-anchor="middle">KITCHEN | BATHROOM | HOME REPAIR</text>
    <text class="phone phone--rear" x="390" y="450" font-size="84" fill="var(--wrap-white)" text-anchor="middle">555 014 7720</text>
    <text class="web-address" x="390" y="640" font-size="34" fill="var(--ink-soft)" text-anchor="middle">kestreldunmore.com</text>
    <text class="tagline" x="390" y="690" font-size="28" fill="var(--wrap-black)" text-anchor="middle">MEASURED TWICE,</text>
    <text class="tagline" x="390" y="728" font-size="28" fill="var(--wrap-black)" text-anchor="middle">BUILT TO LAST FOR YEARS</text>
  </svg>

  <svg class="panel panel--door" viewBox="0 0 400 400" xmlns="http://www.w3.org/2000/svg">
    <rect class="door-base" width="400" height="400" fill="var(--wrap-white)"/>
    <text class="brand-name" x="200" y="185" font-size="34" fill="var(--ink-dark)" text-anchor="middle">KESTREL &amp;</text>
    <text class="brand-name" x="200" y="225" font-size="34" fill="var(--ink-dark)" text-anchor="middle">DUNMORE</text>
    <text class="services" x="200" y="258" font-size="15" fill="var(--wrap-black)" text-anchor="middle">KITCHEN | BATHROOM | HOME REPAIR</text>
  </svg>

  <svg class="panel panel--hood" viewBox="0 0 660 300" xmlns="http://www.w3.org/2000/svg">
    <rect class="hood-base" width="660" height="300" fill="var(--wrap-white)"/>
    <text class="brand-name" x="330" y="130" font-size="42" fill="var(--ink-dark)" text-anchor="middle">KESTREL &amp;</text>
    <text class="brand-name" x="330" y="180" font-size="42" fill="var(--ink-dark)" text-anchor="middle">DUNMORE</text>
    <text class="services" x="330" y="218" font-size="20" fill="var(--wrap-black)" text-anchor="middle">KITCHEN | BATHROOM | HOME REPAIR</text>
  </svg>

</main>
</body>
</html>
```